Corporate Dinner Invite at Verolla for PMV

PMV is hosting a corporate dinner at the BRQ Conference and we need an email attachment invite for the event. Please use some images from this site for inspiration: https://www.verollaexample.com/fernparlor/

Invite Title:
Join us for dinner!

Event Details:
Tuesday, October 24th 2023 at 6:30pm
Verolla Chicago, Fern Parlor
347 W Harlow Ave, Chicago, IL 60622

Target Market(s)

Corporate Audience

Font styles to use
Script

Colors
0054AA
0677BA
7BADD7
CADEEF
E8F1F8

Requirements
Must have
• PMV logo, event date / time, event location details, photo(s) from Fern Parlor

```html
<!DOCTYPE html>
<html lang="en">
<head>
<meta charset="utf-8">
<title>PMV Dinner Invitation</title>
<link rel="stylesheet" href="https://fonts.googleapis.com/css2?family=Alex+Brush&family=Cinzel:wght@400;700&display=swap">
<style>
  :root {
    --navy-deep: #071638;
    --navy: #0d1f4f;
    --navy-glow: #4a5675;
    --accent-blue: #3d7fe6;
    --label-blue: #1d48b5;
    --rule-blue: #2a5a9a;
    --white: #ffffff;
    --photo-dark: #141a0c;
    --photo-olive: #5a6a12;
    --photo-lime: #c8d84a;
    --photo-violet: #8a3ca8;
    --photo-wood: #4a2e12;
  }
  html, body {
    margin: 0;
    padding: 0;
    overflow: hidden;
    background: var(--navy-deep);
  }
  .invite {
    position: relative;
    width: 1200px;
    height: 797px;
    overflow: hidden;
    background:
      radial-gradient(ellipse 260px 220px at 737px 0px, var(--navy-glow) 0%, rgba(74,86,117,0) 100%),
      linear-gradient(180deg, var(--navy) 0%, var(--navy-deep) 100%);
    font-family: "Cinzel", serif;
    color: var(--white);
  }
  .invite__art {
    position: absolute;
    inset: 0;
  }
  .brand {
    position: absolute;
    left: 0;
    width: 100%;
    top: 58px;
    margin-left: 218px;
    display: flex;
    justify-content: center;
    align-items: center;
    gap: 12px;
    width: 1200px;
    margin-left: 0;
    padding-left: 436px;
    box-sizing: border-box;
  }
  .brand__mark {
    width: 30px;
    height: 30px;
    background: var(--accent-blue);
  }
  .brand__name {
    font-family: "Cinzel", serif;
    font-weight: 700;
    font-size: 40px;
    letter-spacing: 3px;
    color: var(--accent-blue);
  }
  .title {
    position: absolute;
    left: 520px;
    top: 118px;
    width: 590px;
    margin: 0;
    font-family: "Alex Brush", cursive;
    font-weight: 400;
    font-size: 100px;
    line-height: 1;
    white-space: nowrap;
    text-align: center;
  }
  .title__lead { color: var(--accent-blue); }
  .title__main { color: var(--white); }
  .details-band {
    position: absolute;
    left: 528px;
    top: 279px;
    width: 580px;
    height: 104px;
    background: linear-gradient(90deg,
      rgba(61,127,230,0) 0%,
      var(--accent-blue) 14%,
      var(--accent-blue) 82%,
      rgba(61,127,230,0) 100%);
    display: flex;
    align-items: center;
    justify-content: center;
  }
  .details-band__heading {
    margin: 0;
    font-family: "Alex Brush", cursive;
    font-weight: 400;
    font-size: 64px;
    color: var(--white);
    line-height: 1;
    padding-right: 10px;
  }
  .rule {
    position: absolute;
    left: 513px;
    width: 590px;
    height: 2px;
    background: linear-gradient(90deg, rgba(42,90,154,0) 0%, var(--rule-blue) 8%, var(--rule-blue) 92%, rgba(42,90,154,0) 100%);
  }
  .rule--one { top: 441px; }
  .rule--two { top: 537px; }
  .rule--three { top: 634px; }
  .detail {
    position: absolute;
    left: 537px;
    display: flex;
    align-items: center;
  }
  .detail__label {
    width: 123px;
    height: 37px;
    border: 2px solid var(--label-blue);
    display: flex;
    align-items: center;
    justify-content: center;
    font-weight: 700;
    font-size: 20px;
    letter-spacing: 2px;
    color: var(--accent-blue);
  }
  .detail__value {
    margin-left: 34px;
    font-weight: 400;
    letter-spacing: 1px;
    color: var(--white);
    line-height: 1.02;
  }
  .detail--date { top: 470px; }
  .detail--date .detail__value { font-size: 26px; }
  .detail--time { top: 565px; }
  .detail--time .detail__value { font-size: 38px; margin-left: 38px; }
  .detail--venue { top: 678px; }
  .detail--venue .detail__value { font-size: 24.5px; margin-left: 28px; font-style: normal; }
</style>
</head>
<body>
<main class="invite">
  <svg class="invite__art" width="1200" height="797" viewBox="0 0 1200 797" aria-hidden="false">
    <defs>
      <radialGradient id="photoTone" cx="0.3" cy="0.25" r="0.9">
        <stop offset="0" stop-color="var(--photo-lime)"/>
        <stop offset="0.3" stop-color="var(--photo-olive)"/>
        <stop offset="0.6" stop-color="var(--photo-dark)"/>
        <stop offset="0.8" stop-color="var(--photo-violet)"/>
        <stop offset="1" stop-color="var(--photo-wood)"/>
      </radialGradient>
    </defs>
    <polygon role="img" aria-label="Photo of cocktails garnished with strawberry and lime on a bar table at Fern Parlor, with warm bokeh lights behind"
             points="0,0 569,0 348,432 338,450 523,797 0,797" fill="url(#photoTone)"/>
    <polygon class="edge-stripe" points="338,450 348,432 551,797 523,797" fill="var(--accent-blue)"/>
  </svg>

  <div class="brand">
    <span class="brand__mark"></span>
    <span class="brand__name">PMV</span>
  </div>

  <h1 class="title"><span class="title__lead">Join us</span> <span class="title__main">for Dinner</span></h1>

  <div class="details-band">
    <h2 class="details-band__heading">Event Details</h2>
  </div>

  <div class="rule rule--one"></div>
  <div class="rule rule--two"></div>
  <div class="rule rule--three"></div>

  <div class="detail detail--date">
    <span class="detail__label">DATE</span>
    <span class="detail__value">TUESDAY, OCTOBER 24TH 2023</span>
  </div>

  <div class="detail detail--time">
    <span class="detail__label">TIME</span>
    <span class="detail__value">6:30PM</span>
  </div>

  <div class="detail detail--venue">
    <span class="detail__label">VENUE</span>
    <address class="detail__value">VEROLLA CHICAGO, FERN PARLOR<br>347 W HARLOW AVE, CHICAGO, IL 60622</address>
  </div>
</main>
</body>
</html>
```